Business Cards for an 'affordable luxury' inner city home builder in Calgary.

We need a business card design that emulates the progressive, innovative, culture of our company and the modern style of our homes. Use our website www.velmarcrest-ab.com as a reference for the product we build.

Our company builds homes in the inner city space of Calgary, Alberta. We build affordable luxury.

Target Market(s)

Young professional Families

Contact Information for Business Card

Try to maintain consistency with the logo font and the card font.

Requirements
Must have
• The details must include: Name, education, title, phone number, website and email (Address is not as important)
• The design must be uniques (like our logo), elegant, sophisticated and modern.

```html
<!DOCTYPE html>
<html lang="en">
<head>
<meta charset="utf-8">
<title>Velmarcrest Custom Homes – Business Card</title>
<link href="https://fonts.googleapis.com/css2?family=Montserrat:wght@500&family=Source+Sans+3:wght@400;600;700&display=swap" rel="stylesheet">
<style>
  :root {
    --backdrop: #6d7680;
    --card: #ffffff;
    --ink: #111111;
    --grey-mid: #858585;
    --grey-light: #c4c4c4;
    --grey-dark: #3a3a3a;
  }
  * { margin: 0; padding: 0; box-sizing: border-box; }
  html, body {
    width: 1200px; height: 2400px; overflow: hidden;
    background: var(--backdrop);
  }
  .canvas { position: relative; width: 1200px; height: 2400px; }
  .card {
    position: absolute; left: 100px; width: 1000px; height: 553px;
    background: var(--card); overflow: hidden;
    box-shadow: 0 4px 14px rgba(0,0,0,.35);
  }
  .card--front { top: 520px; }
  .card--back { top: 1330px; }

  .brand-field {
    position: absolute;
    background: linear-gradient(160deg, var(--grey-light) 0%, var(--grey-mid) 55%, var(--grey-dark) 100%);
    opacity: .55;
  }
  .card--front .brand-field { left: 0; top: 0; width: 320px; height: 553px; }
  .card--back .brand-field { right: 0; top: 0; width: 290px; height: 553px; }

  .wordmark {
    position: absolute; display: flex; align-items: center; gap: 22px;
    font-family: "Montserrat", sans-serif; font-weight: 500;
    color: var(--ink); text-transform: uppercase; letter-spacing: .02em;
  }
  .wordmark__square { background: var(--ink); flex: none; }
  .card--front .wordmark { left: 570px; top: 56px; font-size: 25px; line-height: 27px; }
  .card--front .wordmark__square { width: 70px; height: 70px; }
  .card--back .wordmark { left: 103px; top: 215px; font-size: 35px; line-height: 40px; gap: 38px; }
  .card--back .wordmark__square { width: 118px; height: 118px; }

  .person {
    position: absolute; left: 570px; top: 196px;
    font-family: "Source Sans 3", sans-serif; color: var(--ink);
  }
  .person__name { font-size: 46px; font-weight: 700; line-height: 50px; }
  .person__name-last { color: var(--grey-mid); }
  .person__title { font-size: 21px; font-weight: 600; line-height: 26px; }

  .contact-list {
    position: absolute; left: 570px; top: 313px; list-style: none;
    font-family: "Source Sans 3", sans-serif; font-size: 22px; color: var(--ink);
  }
  .contact-list li { display: flex; align-items: center; gap: 12px; height: 46px; }
  .contact-list svg { width: 30px; height: 30px; flex: none; }
</style>
</head>
<body>
<div class="canvas">

  <section class="card card--front" aria-label="Business card front">
    <div class="brand-field" role="img" aria-label="Large brand decoration area"></div>

    <div class="wordmark">
      <span class="wordmark__square"></span>
      <span>Velmarcrest<br>Custom<br>Homes Ltd</span>
    </div>

    <div class="person">
      <p class="person__name">Your <span class="person__name-last">Namehere</span></p>
      <p class="person__title">Designation</p>
    </div>

    <ul class="contact-list">
      <li>
        <svg viewBox="0 0 30 30" aria-hidden="true"><rect width="30" height="30" rx="4" fill="#111"/><path d="M9 7c1-.6 2-.4 2.6.5l1.6 2.6c.4.7.3 1.5-.3 2l-1 .9c.9 2 2.3 3.5 4.2 4.5l1-1c.5-.6 1.3-.7 2-.3l2.6 1.6c.8.6 1 1.7.4 2.6l-1 1.3c-.7.9-2 1.3-3.1.9C12.7 21.6 9 17.9 7.3 12.6c-.4-1.1 0-2.4.8-3.1z" fill="#fff"/></svg>
        <span>403-555-0148</span>
      </li>
      <li>
        <svg viewBox="0 0 30 30" aria-hidden="true"><rect width="30" height="30" rx="4" fill="#111"/><rect x="7" y="9.5" width="16" height="11" fill="#fff"/><path d="M7 9.5l8 6.5 8-6.5M7 20.5l6-5M23 20.5l-6-5" stroke="#111" stroke-width="1.4" fill="none"/></svg>
        <span>projects@velmarcrest-ab.com</span>
      </li>
      <li>
        <svg viewBox="0 0 30 30" aria-hidden="true"><rect width="30" height="30" rx="4" fill="#111"/><g stroke="#fff" stroke-width="1.4" fill="none"><circle cx="15" cy="15" r="8"/><ellipse cx="15" cy="15" rx="3.5" ry="8"/><path d="M7 15h16M8.5 11h13M8.5 19h13"/></g></svg>
        <span>www.velmarcrest-ab.com</span>
      </li>
      <li>
        <svg viewBox="0 0 30 30" aria-hidden="true"><rect width="30" height="30" rx="4" fill="#111"/><path d="M15 6.5a6 6 0 0 1 6 6c0 4.5-6 11-6 11s-6-6.5-6-11a6 6 0 0 1 6-6z" fill="#fff"/><circle cx="15" cy="12.5" r="2.3" fill="#111"/></svg>
        <span>218 14 Ave NE, Calgary, AB</span>
      </li>
    </ul>
  </section>

  <section class="card card--back" aria-label="Business card back">
    <div class="wordmark">
      <span class="wordmark__square"></span>
      <span>Velmarcrest<br>Custom<br>Homes Ltd</span>
    </div>
    <div class="brand-field" role="img" aria-label="Large brand decoration area"></div>
  </section>

</div>
</body>
</html>
```